Book cover design : The Copper Lantern

We need a striking book cover design for a book which will be published via Orvello Reader and as a paperback. The book is a simple short story - ghost story - for children. The book is set in a contemporary English town.

The title of the book is : The Copper Lantern
The author is: Walter Finch

The book is a story book, for children, aged approximately 11-15 years old.
It is a ghost story, but not too scary.

Text to go on the front cover:
The Copper Lantern

Walter Finch

Text to go on the back cover :

The Copper Lantern; a ghost story of controlled readability for students aged 11 to 15 years, (catch-up reading). Also for students of English as a foreign language.

Target Market(s)

A ghost story of controlled readability for students aged 11 to 15 years, (catch-up reading). Also for students of English as a foreign language.

```html
<!DOCTYPE html>
<html lang="en">
<head>
<meta charset="utf-8">
<title>The Copper Lantern — Walter Finch</title>
<link rel="stylesheet" href="https://fonts.googleapis.com/css2?family=Anton&family=Oranienbaum&display=swap">
<style>
  :root {
    --page-bg: #e6e6e4;
    --cover-night: #14111c;
    --cover-dusk: #2a1a2c;
    --glow-orange: #e2741c;
    --glow-amber: #f2a93a;
    --ember-red: #d4233f;
    --spirit-pale: #eef4f6;
    --spirit-blue: #9fc4d8;
    --title-yellow: #ece02e;
    --title-shadow: #c21d3a;
    --type-white: #f2f0ec;
  }
  html, body {
    margin: 0;
    width: 1200px;
    height: 800px;
    overflow: hidden;
    background: var(--page-bg);
  }
  .canvas {
    position: relative;
    width: 1200px;
    height: 800px;
    display: flex;
    align-items: center;
    justify-content: center;
  }
  .book-cover {
    position: relative;
    width: 505px;
    height: 740px;
    overflow: hidden;
    background: var(--cover-night);
  }
  .cover-artwork {
    position: absolute;
    inset: 0;
    width: 505px;
    height: 740px;
    display: block;
  }
  .ember-spatter {
    position: absolute;
    inset: 0;
    background:
      radial-gradient(circle at 5% 60%, rgba(212,35,63,.4), transparent 13%),
      radial-gradient(circle at 97% 52%, rgba(212,35,63,.4), transparent 11%),
      radial-gradient(circle at 92% 80%, rgba(70,50,120,.4), transparent 17%),
      radial-gradient(circle at 6% 86%, rgba(70,50,120,.35), transparent 15%);
  }
  .cover-text {
    position: absolute;
    left: 0;
    right: 0;
    margin: 0;
    text-align: center;
    white-space: nowrap;
  }
  .title-article {
    top: 470px;
    font-family: "Oranienbaum", serif;
    font-size: 38px;
    letter-spacing: 2px;
    color: var(--type-white);
    line-height: 1;
  }
  .title-main {
    top: 510px;
    font-family: "Anton", sans-serif;
    font-weight: 400;
    font-size: 74px;
    line-height: 1.2;
    color: var(--title-yellow);
    text-shadow: 4px 3px 0 var(--title-shadow);
    letter-spacing: 0.5px;
  }
  .author-name {
    top: 648px;
    font-family: "Oranienbaum", serif;
    font-size: 58px;
    line-height: 1;
    letter-spacing: 3px;
    color: var(--type-white);
  }
</style>
</head>
<body>
<main class="canvas">
  <article class="book-cover">
    <svg class="cover-artwork" viewBox="0 0 505 740"
         role="img" aria-label="Illustration: a pale ghostly lady in a tattered white dress floating above a graveyard, bare trees and bats silhouetted against a glowing orange moon">
      <defs>
        <radialGradient id="moonGlow" cx="252" cy="250" r="300" gradientUnits="userSpaceOnUse">
          <stop offset="0%" stop-color="var(--glow-amber)"/>
          <stop offset="30%" stop-color="var(--glow-orange)"/>
          <stop offset="62%" stop-color="#4a2530"/>
          <stop offset="100%" stop-color="var(--cover-night)"/>
        </radialGradient>
        <linearGradient id="sideShade" x1="0" y1="0" x2="1" y2="0">
          <stop offset="0%" stop-color="var(--cover-night)" stop-opacity=".85"/>
          <stop offset="22%" stop-color="var(--cover-night)" stop-opacity="0"/>
          <stop offset="78%" stop-color="var(--cover-night)" stop-opacity="0"/>
          <stop offset="100%" stop-color="var(--cover-night)" stop-opacity=".85"/>
        </linearGradient>
        <linearGradient id="groundFade" x1="0" y1="0" x2="0" y2="1">
          <stop offset="0%" stop-color="var(--cover-night)" stop-opacity="0"/>
          <stop offset="100%" stop-color="var(--cover-night)"/>
        </linearGradient>
        <linearGradient id="spiritGlow" x1="0" y1="0" x2="0" y2="1">
          <stop offset="0%" stop-color="var(--spirit-pale)" stop-opacity=".95"/>
          <stop offset="70%" stop-color="var(--spirit-blue)" stop-opacity=".8"/>
          <stop offset="100%" stop-color="var(--spirit-blue)" stop-opacity="0"/>
        </linearGradient>
        <radialGradient id="emberPool" cx="50%" cy="50%" r="50%">
          <stop offset="0%" stop-color="var(--ember-red)" stop-opacity=".9"/>
          <stop offset="100%" stop-color="var(--ember-red)" stop-opacity="0"/>
        </radialGradient>
      </defs>
      <rect width="505" height="740" fill="url(#moonGlow)"/>
      <rect width="505" height="740" fill="url(#sideShade)"/>
      <rect y="330" width="505" height="410" fill="url(#groundFade)"/>
      <ellipse cx="258" cy="456" rx="130" ry="12" fill="url(#emberPool)"/>
      <rect x="200" y="60" width="130" height="390" rx="60" fill="url(#spiritGlow)"/>
    </svg>
    <div class="ember-spatter"></div>
    <div class="cover-text title-article">THE</div>
    <h1 class="cover-text title-main">COPPER LANTERN</h1>
    <div class="cover-text author-name">WALTER FINCH</div>
  </article>
</main>
</body>
</html>
```